"sweetpailo!" hand crafted, premium gelato needs a delicious design!

SweetPailo!
Hand Crafted, Premium, Delicious (tag line to be included)

We are artisan gelato craftsmen, passionate about the art of making gelato. Our philosophy to crafting our premium gelato is pure and simple.
Always use quality fresh ingredients
Keep learning, always improving and honing our gelato crafting skills
We believe that this simple philosophy is the key to our Delicious, Premium and Authentic gelato that is SweetPailo!

Where possible, we source our key ingredients from local producers who in their own right are proud and passionate about their produce.

The logo should be clean and communicate a premium, artisan, hand crafted product.

I will require a front label which describes the flavor of the gelato and a rear ingredients/nutritional facts label.

The rear label needs to be easily modifiable according to the flavor and ingredients used, as we add to our flavor list.

There should also be a space to insert a nutrition label - I've uploaded an example of a nutrition label

As an example for rear label

___________________________________________________________________________
Our artisan Gelato is proudly hand crafted in small batches with love, passion and with local Australian produce whenever possible. We use Fresh Milk and Pure Cream sourced from local producers who are equally passionate about their produce.

We only use All Natural ingredients. Free from any artificial colours, flavours, and preservatives.

Ingredients
Fresh Milk, Pure Cream, Skim Milk Powder, Sugar, Dextrose, Japanese Matcha, Arrowroot Flour. Guar Gum

Contains Milk, Wheat

Although we do not use nuts, some of the ingredients we use may have been processed on equipment that may have processed nuts.

Best Stored Frozen at minus 18°C

We would love to hear from you!
www.sweetpailo.com.au
gelato@sweetpailo.com.au
(place facebook logo here)

Example of a label I like:

http://www.wrapmuseboard.example/tondo-artisan-gelato.html/

I would like to showcase the end product as much as possible so the label should be transparent and enhance the flavor of the gelato. A small graphic complimenting the key ingredient the flavor would be enhancing the product.

Some of the examples of the flavors we have are
Japanese Matcha * this will be the main flavour
Kestrel Hills Chocolate Bar
Dunmore Creek Salted Caramel
Vanilla Bean

Please note that there is future paid opportunity to make modifications to the front label and ingredients label as we keep adding flavors so I am looking for a designer that I can have a long term partnership with. Thanks! Added Wednesday, October 12, 2016

Target Market(s)

Retail space looking for a premium alternative to the high end ice cream. People who appreciate artisan products

Logo Text

SweetPailo!- Premium, Hand Crafted, Delicious

Requirements
Must have
• must highlight the key ingredient of each flavor

```html
<!DOCTYPE html>
<html lang="en">
<head>
<meta charset="utf-8">
<title>SweetPailo! – Vanilla Bean Labels</title>
<link href="https://fonts.googleapis.com/css2?family=Amatic+SC:wght@700&family=Oswald:wght@400;500;600&display=swap" rel="stylesheet">
<style>
  :root{
    --page:#f6f6f6;
    --ink:#161616;
    --label:#f3ebcf;
    --label-edge:#e6dbb6;
    --brown:#a38b5a;
    --brown-soft:#c8b68c;
  }
  *{margin:0;padding:0;box-sizing:border-box}
  html,body{width:1200px;height:848px;overflow:hidden;background:var(--page)}
  .canvas{position:relative;width:1200px;height:848px}

  .brand-header{
    position:absolute;top:62px;left:0;width:100%;text-align:center;
    font-family:'Oswald',sans-serif;font-weight:400;font-size:52px;line-height:1;
    color:var(--ink);letter-spacing:2px;
  }

  .label{
    position:absolute;top:360px;width:296px;height:288px;background:var(--label);
    border:1px solid var(--label-edge);border-radius:0 0 26px 26px;
    color:var(--brown);overflow:hidden;
  }
  .label--front{left:160px}
  .label--rear{left:748px}

  /* front label */
  .front-brand{
    position:absolute;top:44px;width:100%;text-align:center;
    font-family:'Oswald',sans-serif;font-weight:400;font-size:17px;line-height:1;letter-spacing:1px;
  }
  .flavour{
    position:absolute;top:96px;width:100%;text-align:center;
    font-family:'Oswald',sans-serif;font-weight:600;line-height:.95;
  }
  .flavour-top{display:block;font-size:38px;font-weight:500}
  .flavour-bottom{display:block;font-size:60px;letter-spacing:1px}
  .ingredient-art{
    position:absolute;top:96px;width:64px;height:120px;border-radius:40% 40% 30% 30%;
    background:radial-gradient(circle at 50% 40%,var(--brown) 0%,var(--brown-soft) 60%,var(--label) 100%);
    opacity:.75;
  }
  .ingredient-art--left{left:14px}
  .ingredient-art--right{right:14px}
  .volume{
    position:absolute;top:256px;width:100%;text-align:center;
    font-family:'Oswald',sans-serif;font-weight:500;font-size:14px;line-height:1;
  }

  /* rear label */
  .rear{
    padding:10px 10px 0;text-align:center;
    font-family:'Amatic SC',cursive;font-weight:700;font-size:10.5px;line-height:1.05;
  }
  .rear p{margin-bottom:2px}
  .rule{height:1px;background:var(--brown);margin:4px 48px}
  .rear h3{font-size:12.5px;font-weight:700;margin-bottom:2px}
  .servings{text-align:left;margin:2px 0 3px 30px}
  .servings span{display:inline-block;width:80px}
  .nutrition{margin:0 auto;border-collapse:collapse;font-size:10px;text-align:left;width:222px}
  .nutrition th{font-weight:700;padding:1px 4px;border-bottom:1px solid var(--brown);vertical-align:bottom;line-height:1}
  .nutrition td{padding:0 4px;line-height:.95}
  .nutrition td+td,.nutrition th+th{border-left:1px solid var(--brown)}
  .nutrition .indent{padding-left:16px}
</style>
</head>
<body>
<main class="canvas">
  <h1 class="brand-header">SweetPailo!</h1>

  <section class="label label--front">
    <div class="front-brand">SweetPailo!</div>
    <div class="ingredient-art ingredient-art--left" role="img" aria-label="Vanilla flower and pod illustration"></div>
    <h2 class="flavour"><span class="flavour-top">vanilla</span><span class="flavour-bottom">BEAN</span></h2>
    <div class="ingredient-art ingredient-art--right" role="img" aria-label="Vanilla flower and pod illustration"></div>
    <div class="volume">500 ml</div>
  </section>

  <section class="label label--rear">
    <div class="rear">
      <p>Our Gelato is proudly made in Australia with love, passion<br>and with local Australian products whenever possible.<br>We use Fresh Milk and Pure Cream sourced from local producers.<br>No artificial colours, flavours or preservatives<br>are used in our Gelato.</p>
      <div class="rule"></div>
      <h3>Ingredients</h3>
      <p>Tarwin Jersey Fresh Milk, Tarwin Jersey Pure Cream, Skim Milk Powder, Sugar, Glucose, Vanilla Bean, Arrowroot Flour, Guar Gum (may contain traces of nuts).</p>
      <p>Contains Milk, Wheat<br>Best Stored Frozen at minus 18°C</p>
      <div class="rule"></div>
      <h3>Nutrition Information</h3>
      <div class="servings"><span>Servings per package</span>10.00<br><span>Serving size</span>150.00 g</div>
      <table class="nutrition">
        <tr><th></th><th>Average Qty<br>per Serving</th><th>Average Qty<br>per 100 g</th></tr>
        <tr><td>Energy</td><td>1490 kJ</td><td>994 kJ</td></tr>
        <tr><td>Protein</td><td>8.1 g</td><td>5.4 g</td></tr>
        <tr><td>Fat – total</td><td>18.8 g</td><td>12.5 g</td></tr>
        <tr><td class="indent">– saturated</td><td>12.1 g</td><td>8.0 g</td></tr>
        <tr><td>Carbohydrate</td><td>38.3 g</td><td>25.5 g</td></tr>
        <tr><td class="indent">– sugars</td><td>32.1 g</td><td>21.4 g</td></tr>
        <tr><td>Sodium</td><td>0.95 mg</td><td>0.63 mg</td></tr>
      </table>
    </div>
  </section>
</main>
</body>
</html>
```